Business Card Design needed for logo design project

Would like a professional business card for a company involved in financial and latest technologies including CAD design. We would like the card to convey professionalism and communicate that we are involved in up to date technology solutions.

Target Market(s)

Business 2 Business sales

Industry/Entity Type

Financial

Colors

Designer to choose colors to be used in the design.

Requirements
Must have
• Business Name
Logo
Name
Phone
Email
Nice to have
• Website

```html
<!DOCTYPE html>
<html lang="en">
<head>
<meta charset="UTF-8">
<title>Vorantek Business Card</title>
<link href="https://fonts.googleapis.com/css2?family=Ubuntu:wght@400;500;700&display=swap" rel="stylesheet">
<style>
  :root {
    --page-bg: #e9e6e2;
    --card-red: #c9262f;
    --card-red-light: #dc3a42;
    --card-red-dark: #a81c25;
    --ink-white: #ffffff;
    --ink-soft: rgba(255,255,255,0.9);
  }
  * { box-sizing: border-box; margin: 0; padding: 0; }
  html, body {
    width: 1200px; height: 788px; overflow: hidden;
    background: var(--page-bg);
    font-family: "Ubuntu", "Segoe UI", sans-serif;
  }
  .stage {
    width: 1200px; height: 788px;
    display: flex; align-items: center; justify-content: center;
  }
  .card {
    position: relative;
    width: 1000px; height: 571px;
    overflow: hidden;
    color: var(--ink-white);
    box-shadow: 0 10px 30px rgba(0,0,0,0.18);
  }
  .card-pattern {
    position: absolute; inset: 0;
    background: linear-gradient(135deg, var(--card-red-light) 0%, var(--card-red) 45%, var(--card-red-dark) 100%);
  }
  .brand {
    position: absolute; left: 70px; top: 160px;
    font-size: 56px; font-weight: 700; letter-spacing: 2px;
    line-height: 1;
  }
  .person {
    position: absolute; left: 520px; top: 120px;
    display: flex; flex-direction: column; align-items: flex-end;
  }
  .person-name { font-size: 64px; font-weight: 700; line-height: 1; }
  .person-role { font-size: 22px; color: var(--ink-soft); margin-top: 4px; }
  .contact {
    position: absolute;
    display: flex; align-items: center; gap: 12px;
    font-size: 19px; line-height: 22px; color: var(--ink-soft);
    white-space: nowrap;
  }
  .contact svg { width: 22px; height: 22px; flex: none; }
  .c-handle  { left: 720px; top: 262px; }
  .c-chat    { left: 720px; top: 304px; }
  .c-company { left: 490px; top: 318px; }
  .c-phone   { left: 490px; top: 360px; }
  .c-email   { left: 240px; top: 420px; }
  .c-web     { left: 240px; top: 460px; }
  .c-address { left: 240px; top: 510px; font-size: 21px; }
</style>
</head>
<body>
<main class="stage">
  <section class="card">
    <div class="card-pattern" role="img" aria-label="Red low-poly triangle pattern background"></div>

    <div class="brand">VORANTEK</div>

    <div class="person">
      <div class="person-name">Name</div>
      <div class="person-role">(CEO)</div>
    </div>

    <div class="contact c-handle">
      <svg viewBox="0 0 22 22"><circle cx="11" cy="11" r="9" fill="#fff"/></svg>
      <span>@vorantekhq</span>
    </div>
    <div class="contact c-chat">
      <svg viewBox="0 0 22 22"><rect x="2" y="2" width="18" height="18" rx="3" fill="#fff"/></svg>
      <span>vorantek.call</span>
    </div>
    <div class="contact c-company">
      <svg viewBox="0 0 22 22"><rect x="2" y="2" width="18" height="18" rx="2" fill="#fff"/></svg>
      <span>vorantek.team</span>
    </div>
    <div class="contact c-phone">
      <svg viewBox="0 0 22 22"><rect x="6" y="2" width="10" height="18" rx="2" fill="none" stroke="#fff" stroke-width="2"/><circle cx="11" cy="16.5" r="1.2" fill="#fff"/></svg>
      <span>+1 (555) 014 27</span>
    </div>
    <div class="contact c-email">
      <svg viewBox="0 0 22 22"><rect x="2" y="5" width="18" height="12" rx="1.5" fill="#fff"/><path d="M3 6 L11 12 L19 6" fill="none" stroke="#c9262f" stroke-width="1.6"/></svg>
      <span>hello@vorantek.example</span>
    </div>
    <div class="contact c-web">
      <svg viewBox="0 0 22 22"><circle cx="11" cy="11" r="8" fill="none" stroke="#fff" stroke-width="2"/><ellipse cx="11" cy="11" rx="3.5" ry="8" fill="none" stroke="#fff" stroke-width="1.5"/><line x1="3" y1="11" x2="19" y2="11" stroke="#fff" stroke-width="1.5"/></svg>
      <span>www.vorantek.example</span>
    </div>
    <div class="contact c-address">
      <svg viewBox="0 0 22 22"><path d="M2 11 L11 3 L20 11" fill="none" stroke="#fff" stroke-width="2"/><path d="M5 10 V19 H9 V14 H13 V19 H17 V10" fill="#fff"/></svg>
      <span>Suite 12, Harbor Point, Lakeview City, Northland</span>
    </div>
  </section>
</main>
</body>
</html>
```